Pelton|Marsh & Quillan business card contest

We need a logo for an upscale boutique diversified company involved in real estate, investments, cattle, and more. Our businesses DO NOT need to be reflected in the business card nor do we want them noted. This is our logo and colors and we love our logo and colors. Our logo looks best against a black background and we like to include the firm name in our logo usage. importantly, the names Pelton and Marsh are separated by | not / and we use an ampersand not the word and.
On the front of the card, we want to include:
company logo and name (Pelton|Marsh & Quillan)
on the back, we would definitely include:
address, email, cell #
logo and name (smaller size than front)

The variable will be location of individual name and title (mine for example is ) - whether on the front OR on the back. interested in variations from which to choose
Dr. Neil R. Whitcombe, CFA
Scientifique des Fusées Financières

we would like to use contemporary symbols for address, email address, cell # with an option for web site that we do not intend to use initially. we like two sided cards and believe this design should use four rounded corners with the standard size. we prefer thicker card stock and may look at metal.

```html
<!DOCTYPE html>
<html lang="en">
<head>
<meta charset="utf-8">
<title>Pelton|Marsh &amp; Quillan – Business Card</title>
<link rel="stylesheet" href="https://fonts.googleapis.com/css2?family=Lato:wght@400;700&display=swap">
<style>
  :root {
    --backdrop: #2a2a2a;
    --card: #141414;
    --card-edge: #1d1d1d;
    --grey-mark: #6f6f6f;
    --grey-text: #8a8a8a;
    --orange: #d9791c;
    --orange-deep: #a85810;
  }
  * { box-sizing: border-box; margin: 0; padding: 0; }
  html, body {
    width: 1200px; height: 997px; overflow: hidden;
    background: var(--backdrop);
    font-family: "Lato", Arial, sans-serif;
  }
  .stage { position: relative; width: 1200px; height: 997px; }

  .card {
    position: absolute;
    width: 735px; height: 420px;
    background: var(--card);
    border: 1px solid var(--card-edge);
    border-radius: 16px;
    box-shadow: 0 18px 40px rgba(0,0,0,.55);
  }
  .card--front { left: 80px; top: 60px; }
  .card--back  { left: 385px; top: 517px; }

  /* Front: firm name as wordmark */
  .front-wordmark {
    position: absolute; inset: 0;
    display: flex; align-items: center; justify-content: center; gap: 18px;
  }
  .mark-square { width: 34px; height: 34px; background: var(--orange); }
  .front-wordmark .firm-name {
    font-size: 46px; font-weight: 400; color: var(--grey-mark); letter-spacing: 1px;
  }

  /* Back */
  .back-wordmark {
    position: absolute; left: 50px; top: 0; bottom: 0; width: 330px;
    display: flex; align-items: center; gap: 12px;
  }
  .back-wordmark .mark-square { width: 22px; height: 22px; }
  .back-wordmark .firm-name {
    font-size: 25px; font-weight: 400; color: var(--grey-mark);
  }
  .divider {
    position: absolute; left: 400px; top: 105px; width: 2px; height: 210px;
    background: linear-gradient(to bottom, transparent, var(--orange) 50%, transparent);
  }
  .contact { position: absolute; left: 425px; top: 110px; color: var(--grey-text); }
  .contact .person-name { color: var(--orange); font-size: 17px; font-weight: 400; }
  .contact .credentials { font-size: 12px; margin-top: 4px; }
  .contact .office { font-size: 13px; font-weight: 700; margin-top: 18px; }
  .contact .address { font-size: 13px; margin-top: 3px; }
  .contact-list { list-style: none; margin-top: 26px; font-size: 14px; }
  .contact-list li { display: flex; align-items: center; gap: 10px; margin-bottom: 5px; }
  .contact-list svg { width: 13px; height: 13px; fill: var(--orange); flex: none; }
</style>
</head>
<body>
<main class="stage">

  <section class="card card--front" aria-label="Card front">
    <div class="front-wordmark">
      <span class="mark-square"></span>
      <span class="firm-name">Pelton|Marsh &amp; Quillan</span>
    </div>
  </section>

  <section class="card card--back" aria-label="Card back">
    <div class="back-wordmark">
      <span class="mark-square"></span>
      <span class="firm-name">Pelton|Marsh &amp; Quillan</span>
    </div>
    <div class="divider"></div>
    <div class="contact">
      <p class="person-name">Maren Holt-Delacroix</p>
      <p class="credentials">M.Ed., R.Psych.</p>
      <p class="office">The Ashgrove Block</p>
      <p class="address">2210-48 Ave.Box 1147 Red Ridge, AB T2K 4N9</p>
      <ul class="contact-list">
        <li>
          <svg viewBox="0 0 16 16" aria-hidden="true"><path d="M3 1h3l1.5 4-2 1.2a9 9 0 0 0 4.3 4.3L11 8.5l4 1.5v3a2 2 0 0 1-2 2A13 13 0 0 1 1 3a2 2 0 0 1 2-2z"/></svg>
          403.555.0182
        </li>
        <li>
          <svg viewBox="0 0 16 16" aria-hidden="true"><path d="M1 3h14v10H1z M1.5 3.5 8 9l6.5-5.5" stroke="#141414" stroke-width="1.2"/></svg>
          maren@northfieldcounsel.ca
        </li>
        <li>
          <svg viewBox="0 0 16 16" aria-hidden="true"><circle cx="8" cy="8" r="7"/><path d="M1 8h14M8 1c3 3 3 11 0 14M8 1c-3 3-3 11 0 14" stroke="#141414" stroke-width="1" fill="none"/></svg>
          www.northfieldcounsel.ca
        </li>
      </ul>
    </div>
  </section>

</main>
</body>
</html>
```